PowerPoint Template

We would like new powerpoint template for our organization: Fjordvik Data Guild.
Enclosed you find our logo and old template.
Industry/Entity Type
Computer
Requirements
Must have
- 1. Logo
2. Footer (for autor)
3. Font: Variations of ARIAL

```html
<!DOCTYPE html>
<html lang="en">
<head>
<meta charset="utf-8">
<title>New Product Development 2014 – Fjordvik Data Guild</title>
<link rel="stylesheet" href="https://fonts.googleapis.com/css2?family=Arimo:wght@400;700&display=swap">
<style>
  :root {
    --page-bg: #e4e4e4;
    --slide-deep: #0b2a4a;
    --slide-mid: #1f5f8c;
    --slide-light: #2f7fae;
    --panel: #ffffff;
    --ink: #000000;
    --navy: #14284a;
    --brand-square: #e8434a;
    --chart-warm: #f6c944;
    --chart-cool: #8fd3f0;
    --chart-pink: #f07fb4;
  }
  * { box-sizing: border-box; margin: 0; padding: 0; }
  html, body {
    width: 1200px; height: 1000px; overflow: hidden;
    background: var(--page-bg);
    font-family: "Arimo", Arial, sans-serif;
  }
  .slide {
    position: absolute; left: 109px; top: 114px;
    width: 1024px; height: 768px;
    background: radial-gradient(ellipse at 85% 40%, var(--slide-light) 0%, var(--slide-mid) 35%, var(--slide-deep) 90%);
    overflow: hidden;
  }
  .content-panel {
    position: absolute; left: 40px; top: 45px;
    width: 970px; height: 706px;
    background: var(--panel);
    border-radius: 12px;
    box-shadow: 0 2px 8px rgba(0,0,0,.35);
  }
  .brand-tab {
    position: absolute; left: 81px; top: 0;
    width: 158px; height: 243px;
    background: var(--panel);
    border-radius: 0 0 8px 8px;
    box-shadow: 0 4px 12px rgba(0,0,0,.35);
    text-align: center;
  }
  .brand-tab .site {
    margin-top: 46px;
    font-size: 14px; font-weight: 700; color: var(--navy);
  }
  .brand-mark {
    margin: 30px auto 0; width: 130px;
    display: flex; flex-direction: column; align-items: center; gap: 12px;
  }
  .brand-mark .square {
    width: 40px; height: 40px; background: var(--brand-square);
  }
  .brand-mark .name {
    font-size: 20px; font-weight: 700; line-height: 1.15; color: var(--navy);
  }
  .chart-art {
    position: absolute; left: 56px; top: 300px;
    width: 372px; height: 308px;
    border-radius: 40% 30% 20% 40%;
    background:
      radial-gradient(ellipse at 22% 70%, var(--chart-warm) 0%, rgba(246,201,68,0) 45%),
      radial-gradient(ellipse at 70% 45%, var(--chart-pink) 0%, rgba(240,127,180,0) 45%),
      radial-gradient(ellipse at 80% 15%, var(--chart-cool) 0%, rgba(143,211,240,0) 40%),
      #ffffff;
  }
  .intro {
    position: absolute; left: 475px; top: 165px; width: 500px;
    color: var(--ink);
  }
  .intro h1 {
    font-size: 53px; font-weight: 700; line-height: 62px;
  }
  .intro h2 {
    margin-top: 30px;
    font-size: 24px; font-weight: 700;
  }
  .intro p {
    margin-top: 14px;
    font-size: 16px; font-weight: 700; line-height: 32.6px;
  }
  .author-tab {
    position: absolute; left: 669px; top: 721px;
    width: 280px; height: 47px;
    background: var(--panel);
    border-radius: 8px 8px 0 0;
    box-shadow: 0 -2px 8px rgba(0,0,0,.25);
    font-size: 18px; font-weight: 700; color: var(--navy);
    display: flex; align-items: center; justify-content: center;
  }
</style>
</head>
<body>
  <main class="slide">
    <section class="content-panel">
      <div class="chart-art" role="img" aria-label="Colourful 3D pie chart and rising bar chart with an upward trend arrow"></div>
      <div class="intro">
        <h1>New Product<br>Development 2014</h1>
        <h2>A Brief History</h2>
        <p>The FDG is working to improve and renew the special<br>
        offers to the members in accordance with the different<br>
        target groups in the member base. We are working hard to<br>
        promote the Society on the World Wide Web<br>
        (http://fjordvikdata.org/), and at this time we are inte-<br>
        grating more functionality for our governing bodies into<br>
        our Web solution.</p>
      </div>
    </section>
    <header class="brand-tab">
      <div class="site">fjordvikdata.org</div>
      <div class="brand-mark">
        <span class="square"></span>
        <span class="name">Fjordvik Data Guild</span>
      </div>
    </header>
    <footer class="author-tab">Presentation BY. Ms Linnea</footer>
  </main>
</body>
</html>
```